Corvane Jewelers Business Cards

A creative, cool edgy business card for our entire team that says we are a young, hip, luxury jewelry store specializing in diamonds and engagement rings but that we are also personal shoppers and trusted advisors. Our colors are Navy Blue & Platinum

I have included our past business card.

Font styles to use
Serif

Colors
0255a3

Requirements
Nice to have
• A card stock that you can write on with a pen

```html
<!DOCTYPE html>
<html lang="en">
<head>
<meta charset="utf-8">
<title>Corvane Jewelers – Business Cards</title>
<link href="https://fonts.googleapis.com/css2?family=Cinzel:wght@400&family=Noto+Serif:wght@700&family=Open+Sans:wght@400;600&display=swap" rel="stylesheet">
<style>
  :root {
    --navy: #15245f;
    --platinum: #8a8a8c;
    --paper: #ffffff;
    --ink: #2d2d33;
    --backdrop: #eceae6;
  }
  * { margin: 0; padding: 0; box-sizing: border-box; }
  html, body { width: 1200px; height: 900px; overflow: hidden; }
  body { background: var(--backdrop); position: relative; font-family: "Open Sans", Arial, sans-serif; }

  .card {
    position: absolute;
    width: 520px;
    height: 300px;
    border-radius: 4px;
    overflow: hidden;
    box-shadow: 0 6px 20px rgba(0,0,0,0.18);
  }
  .card-front { left: 90px; top: 150px; background: var(--navy); display: flex; align-items: center; justify-content: center; }
  .card-back { left: 590px; top: 450px; background: var(--paper); }

  .brand-name {
    font-family: "Cinzel", Georgia, serif;
    font-weight: 400;
    letter-spacing: 1px;
    white-space: nowrap;
  }
  .card-front .brand-name { color: var(--paper); font-size: 34px; }
  .card-back .brand-name { position: absolute; left: 300px; top: 100px; color: var(--navy); font-size: 21px; }

  .wave { position: absolute; inset: 0; width: 520px; height: 300px; }

  .person { position: absolute; left: 40px; top: 62px; }
  .person-name { font-family: "Noto Serif", Georgia, serif; font-weight: 700; font-size: 21px; color: var(--navy); letter-spacing: 0.5px; line-height: 1; }
  .person-title { font-size: 11.5px; color: var(--platinum); letter-spacing: 0.4px; margin-top: 4px; text-transform: uppercase; }

  .contact { position: absolute; left: 40px; top: 150px; list-style: none; color: var(--navy); font-size: 15px; line-height: 19px; }
  .contact li { display: flex; align-items: center; gap: 5px; }
  .contact svg { width: 12px; height: 12px; fill: var(--navy); flex: none; }

  .address { position: absolute; left: 40px; top: 218px; font-size: 15px; line-height: 19px; color: var(--ink); font-style: normal; }

  .website { position: absolute; right: 26px; top: 244px; font-size: 12.5px; color: var(--paper); }
</style>
</head>
<body>
  <section class="card card-front">
    <span class="brand-name">Corvane Jewelers</span>
  </section>

  <section class="card card-back">
    <svg class="wave" viewBox="0 0 520 300" aria-hidden="true">
      <path d="M70,300 C200,282 370,250 490,180 L505,172 C390,252 220,290 95,300 Z" fill="var(--platinum)"/>
      <path d="M110,300 C240,290 400,250 520,162 L520,300 Z" fill="var(--navy)"/>
    </svg>

    <div class="person">
      <h1 class="person-name">ELLIOT MARSH</h1>
      <p class="person-title">Managing Director</p>
    </div>

    <ul class="contact">
      <li><svg viewBox="0 0 12 12"><path d="M1,4 C1,2 3,1 6,1 C9,1 11,2 11,4 L9,5 L8,3.5 L4,3.5 L3,5 Z M3,6 L9,6 L10,11 L2,11 Z"/></svg>044-555 018 247</li>
      <li><svg viewBox="0 0 12 12"><path d="M3,0.5 H9 V11.5 H3 Z M4,2 V9 H8 V2 Z M5.5,9.6 H6.5 V10.6 H5.5 Z"/></svg>044-555 018 247</li>
      <li><svg viewBox="0 0 12 12"><path d="M0.5,2.5 H11.5 V9.5 H0.5 Z M1.5,3.3 L6,6.6 L10.5,3.3 Z" fill-rule="evenodd"/></svg>hello@corvane.com</li>
    </ul>

    <address class="address">48 Alder Row, Suite 2<br>Westmere, 10482.</address>

    <span class="brand-name">Corvane Jewelers</span>

    <p class="website">www.corvane.com</p>
  </section>
</body>
</html>
```